Incorporate navigation bar into exist index page

I need to add a navigation menu into our index (home page) I up for different ideas or designs. Attached is a screen grab of our index page and a basic example of what I'm trying to achieve however don't follow my bad design.

```html
<!DOCTYPE html>
<html lang="en">
<head>
<meta charset="utf-8">
<title>cellstack — home</title>
<link rel="stylesheet" href="https://fonts.googleapis.com/css2?family=Open+Sans:wght@400;600&family=Arimo:wght@400;700&display=swap">
<style>
  :root {
    --page-bg: #f7f7f7;
    --hero-bg: #e9e9e9;
    --hero-inner: #eeeeee;
    --brand-blue: #3a97d8;
    --tab-top: #8fc8ee;
    --tab-bottom: #3b9ad9;
    --tab-audio-top: #d4d4d4;
    --tab-audio-bottom: #a6a6a6;
    --rule: #1e1e1e;
    --dropdown: #595555;
    --ink: #111111;
    --white: #ffffff;
    --arrow-box: #dcdcdc;
    --dot: #2f6f9e;
  }
  * { box-sizing: border-box; margin: 0; padding: 0; }
  html, body { width: 1200px; height: 659px; overflow: hidden; }
  body {
    position: relative;
    background: var(--page-bg);
    font-family: "Open Sans", sans-serif;
    color: var(--ink);
  }
  .account-links {
    position: absolute; top: 12px; left: 990px;
    font-family: "Arimo", sans-serif; font-weight: 700; font-size: 15px;
    display: flex; gap: 12px;
  }
  .account-links .divider { font-weight: 700; }
  .brand {
    position: absolute; left: 49px; top: 30px;
    font-family: "Open Sans", sans-serif; font-weight: 600;
    font-size: 62px; line-height: 1; color: var(--brand-blue);
    letter-spacing: -1px;
  }
  .nav-rule {
    position: absolute; left: 182px; top: 94px; width: 969px; height: 5px;
    background: var(--rule);
  }
  .main-nav {
    position: absolute; top: 64px; left: 471px; display: flex; gap: 6px;
    font-family: "Arimo", sans-serif; font-size: 17px; color: var(--white);
  }
  .nav-tab {
    position: relative; width: 164px; height: 30px;
    border-radius: 6px 6px 0 0;
    background: linear-gradient(var(--tab-top), var(--tab-bottom));
    padding: 5px 0 0 10px; white-space: nowrap;
  }
  .nav-tab.is-open { width: 163px; background: linear-gradient(var(--tab-audio-top), var(--tab-audio-bottom)); }
  .nav-tab .marker { font-size: 10px; margin-right: 6px; vertical-align: 2px; }
  .dropdown {
    position: absolute; left: 471px; top: 98px; width: 163px; height: 172px;
    background: var(--dropdown); list-style: none;
    font-family: "Arimo", sans-serif; font-size: 17px; color: var(--white);
    z-index: 2;
  }
  .dropdown li { position: absolute; left: 13px; }
  .band { position: absolute; left: 0; top: 178px; width: 1200px; height: 373px; background: var(--hero-bg); }
  .hero {
    position: absolute; left: 49px; top: 177px; width: 1102px; height: 372px;
    background: radial-gradient(circle at 60% 30%, #f6f6f6, var(--hero-inner) 70%);
    overflow: hidden;
  }
  .hero-title {
    position: absolute; left: 63px; top: 57px;
    font-size: 24px; font-weight: 600; text-transform: uppercase; letter-spacing: 0.2px;
  }
  .hero-sub { position: absolute; left: 65px; top: 95px; font-size: 21px; }
  .slide-arrow {
    position: absolute; top: 152px; width: 46px; height: 86px; background: var(--arrow-box);
    display: flex; align-items: center; justify-content: center;
  }
  .slide-arrow.prev { left: 0; }
  .slide-arrow.next { right: 0; }
  .label-band {
    position: absolute; left: 0; top: 319px; width: 1102px; height: 53px; background: var(--brand-blue);
  }
  .product {
    position: absolute; top: 178px; width: 146px; text-align: center;
  }
  .product-disc {
    width: 146px; height: 146px; border-radius: 50%; background: var(--white);
    display: flex; align-items: center; justify-content: center;
    box-shadow: 0 1px 3px rgba(0,0,0,0.08);
  }
  .product-photo { width: 96px; height: 80px; border-radius: 12px; background: linear-gradient(#d9d9d9, #bdbdbd); }
  .product-name {
    margin-top: 6px; font-size: 15px; line-height: 18px; color: var(--white);
  }
  .slide-dots { position: absolute; left: 1004px; top: 328px; display: flex; gap: 14px; }
  .slide-dots span { width: 15px; height: 15px; border-radius: 50%; background: var(--dot); }
  .slide-dots span.active { background: #9db0e8; }
  .shop-line {
    position: absolute; left: 0; top: 593px; width: 1200px; text-align: center;
    font-family: "Arimo", sans-serif; font-size: 23px;
  }
</style>
</head>
<body>
  <nav class="account-links"><span>My Cart</span><span class="divider">|</span><span>Login</span></nav>

  <div class="brand">cellstack</div>

  <div class="band"></div>

  <ul class="main-nav" style="list-style:none">
    <li class="nav-tab is-open"><span class="marker">▼</span>audio products</li>
    <li class="nav-tab"><span class="marker">▼</span>mobile products</li>
    <li class="nav-tab"><span class="marker">▼</span>specials</li>
    <li class="nav-tab"><span class="marker">●</span>contact us</li>
  </ul>
  <div class="nav-rule"></div>

  <ul class="dropdown">
    <li style="top:22px">HDMI cables</li>
    <li style="top:76px">HDMI adapters</li>
    <li style="top:130px">HDMI splitters</li>
  </ul>

  <section class="hero">
    <h1 class="hero-title">Ready for a new smart phone?</h1>
    <p class="hero-sub">Then get your hands on these great accessories!!</p>

    <div class="label-band"></div>

    <div class="slide-arrow prev">
      <svg width="10" height="14" viewBox="0 0 10 14"><path d="M8 1 2 7l6 6" fill="none" stroke="#fff" stroke-width="2.5"/></svg>
    </div>
    <div class="slide-arrow next">
      <svg width="10" height="14" viewBox="0 0 10 14"><path d="M2 1l6 6-6 6" fill="none" stroke="#fff" stroke-width="2.5"/></svg>
    </div>

    <div class="product" style="left:292px">
      <div class="product-disc"><div class="product-photo" role="img" aria-label="Micro USB adapter cable product photo"></div></div>
      <p class="product-name">Micro USB<br>Adapters</p>
    </div>
    <div class="product" style="left:455px">
      <div class="product-disc"><div class="product-photo" role="img" aria-label="30-pin adapter product photo"></div></div>
      <p class="product-name">30Pin Adapters</p>
    </div>
    <div class="product" style="left:616px">
      <div class="product-disc"><div class="product-photo" role="img" aria-label="Multi charging cable product photo"></div></div>
      <p class="product-name">Multi Charging<br>Cable</p>
    </div>
    <div class="product" style="left:776px">
      <div class="product-disc"><div class="product-photo" role="img" aria-label="Phone docking station product photo"></div></div>
      <p class="product-name">Docking Station</p>
    </div>
    <div class="product" style="left:935px">
      <div class="product-disc"><div class="product-photo" role="img" aria-label="USB wall charger product photo"></div></div>
      <p class="product-name">USB Wall<br>Chargers</p>
    </div>

    <div class="slide-dots"><span class="active"></span><span></span><span></span></div>
  </section>

  <p class="shop-line"><strong>Shop now</strong> - Simply click on your mobile phone brand</p>
</body>
</html>
```